Charged by courts for driving with suspended license

To be seen by judges and lawyers. Would like some consistency between the brochures which is why we have used same images in places.

Target Market(s)

Lawyers, judges

Industry/Entity Type

legal, auto

Font styles to use
Sans Serif

Requirements
Nice to have
• I like the gears graphic I have used, but open to other ideas. Should be less industrial/automotive rather reflect mentally Turning Point as clients need to change driving behaviour
Should not have
• images with manufacturers names etc. Maybe not have bright colours that are fun or summery as this si for judges, legal profession and must be serious, professional and stately

```html
<!DOCTYPE html>
<html lang="en">
<head>
<meta charset="utf-8">
<title>Turning Point – Suspended Licence Course Brochure</title>
<link rel="stylesheet" href="https://fonts.googleapis.com/css2?family=Libre+Baskerville:ital,wght@0,400;0,700;1,400;1,700&family=Tinos:ital,wght@0,400;0,700;1,400;1,700&family=Roboto:wght@700;900&display=swap">
<style>
:root{
  --stage:#b9b9b9;
  --navy-deep:#0b1c3f;
  --navy:#0f2f55;
  --ocean:#0e4a70;
  --teal:#1a8cab;
  --ink:#ffffff;
  --ink-soft:#dbe8f2;
  --frame:rgba(255,255,255,.85);
}
*{box-sizing:border-box;margin:0;padding:0}
html,body{width:848px;height:1200px;overflow:hidden;background:var(--stage)}
body{position:relative;font-family:"Tinos","Times New Roman",serif;color:var(--ink)}
.sheet{position:absolute;width:731px;height:518px;display:flex;overflow:hidden}
.sheet--outside{left:61px;top:72px}
.sheet--inside{left:60px;top:606px}
.panel{position:relative;height:100%;overflow:hidden}
.panel--left{width:237px;background:linear-gradient(160deg,var(--navy-deep) 0%,#102a55 60%,#143a66 100%)}
.panel--middle{width:248px;background:linear-gradient(170deg,#0b2448 0%,var(--navy) 45%,#11506f 100%)}
.panel--right{width:246px;background:linear-gradient(165deg,#0c3a63 0%,var(--ocean) 45%,var(--teal) 100%)}
.serif-italic{font-family:"Libre Baskerville","Times New Roman",serif;font-style:italic;font-weight:400}
.frame{position:absolute;border:1.5px solid var(--frame);border-radius:7px;display:flex;align-items:center;justify-content:center;text-align:center}

/* outside: background panel */
.background{position:absolute;left:19px;top:45px;width:204px}
.background h2{font-size:10.4px;font-weight:700;font-style:italic;margin-bottom:16px}
.background p{font-size:9.7px;line-height:12.5px;text-align:justify}

/* outside: contact panel */
.motto{left:26px;top:24px;width:194px;height:175px;font-size:18.5px;line-height:23.5px;padding:0 6px}
.contact{position:absolute;left:0;width:100%;text-align:center}
.contact__lead{top:244px;font-size:13.5px;font-style:italic}
.contact__phone{top:272px;font-size:21px;display:flex;justify-content:center;align-items:center;gap:6px}
.contact__web{top:303px;font-size:14px}
.contact__mail{top:330px;font-size:12.6px}

/* outside: cover panel */
.cover-title{left:32px;top:26px;width:202px;height:92px;font-size:27px;line-height:32px}
.cover-kicker{position:absolute;top:142px;left:0;width:100%;text-align:center;font-size:8px;line-height:10px;letter-spacing:.3px}
.cover-subject{position:absolute;top:174px;left:0;width:100%;text-align:center;font-size:16px;line-height:22px;letter-spacing:.5px}
.brand{left:29px;top:235px;width:202px;height:113px;flex-direction:column;gap:6px;padding:8px}
.brand__name{font-family:"Tinos","Times New Roman",serif;font-size:21px;line-height:24px;font-weight:700;color:var(--ink)}
.brand__mark{width:10px;height:10px;border-radius:50%;background:var(--ink)}
.cover-art{position:absolute;left:0;bottom:0;width:246px;height:162px}

/* inside panels */
.inside-text{position:absolute;top:24px;left:20px;width:204px}
.inside-text--middle{left:28px;width:200px;top:26px}
.inside-title{font-size:14.6px;line-height:19px;margin-bottom:12px}
.inside-text h3{font-family:"Tinos","Times New Roman",serif;font-size:10px;font-weight:700;line-height:12.5px;margin:10px 0 9px}
.inside-text p{font-size:8px;line-height:10.4px;margin-bottom:11px;color:var(--ink-soft);text-align:justify}
.inside-text p.intro{margin-bottom:8px}
.inside-text .tight p{margin-bottom:0}
.one-on-one{left:26px;top:101px;width:211px;height:80px;font-size:25px;line-height:34px}
.remote-icon{position:absolute;left:26px;top:256px;width:74px;height:74px}
.remote-label{position:absolute;left:108px;top:278px;font-family:"Roboto",Arial,sans-serif;font-weight:900;font-size:19px;line-height:21px;letter-spacing:.2px}
.remote-label span{display:block}
.remote-label .dark{color:#0b1c3f}
.course-art{position:absolute;left:18px;top:340px;width:208px;height:128px;border-radius:12px}
.cost{position:absolute;left:36px;top:474px;height:23px;padding:0 4px;background:#fff;border-radius:3px;display:flex;align-items:center;gap:6px;font-family:"Roboto",Arial,sans-serif;font-weight:700}
.cost__label{background:#0b1c3f;color:#fff;font-size:8px;padding:3px 5px;border-radius:2px}
.cost__value{color:#0b1c3f;font-size:12px}
</style>
</head>
<body>

<section class="sheet sheet--outside" aria-label="Brochure outside">
  <div class="panel panel--left">
    <div class="background">
      <h2>Our background:</h2>
      <p>Since its inception in 1998, Lane Change Driving School has strived to help drivers maintain their driving independence while leading safe and productive lives. Our motto “building drivers for the long road” drives our vision of helping drivers across industries and at all stages of our driving careers.<br>
      Lane Change started out working with school boards to deliver driver training to beginner drivers. Thousands of students have graduated from our ministry-approved curriculum. We are also ministry-approved to instruct defensive driving (DDC) and driver improvement courses (DIC), for drivers with speeding tickets, demerit points and at fault crashes.<br>
      Lane Change has also evolved to provide comprehensive driver rehabilitation to those who have lost, or are at risk of losing their license for medical reasons. This includes mobility issues requiring adaptive equipment, as well as traumatic crashes resulting in cognitive impairments and PTSD. We work with clients before the courts charged with impaired driving (alcohol, cannabis, opioids), road rage and stunt driving.<br>
      Founder Martin Hale started driving at an early age on his parent’s farm. Driving professionally and doing so safely is in his DNA. Martin has a degree in Business and Psychology from Northvale University and is a certified in-car and in-class driving instructor</p>
    </div>
  </div>

  <div class="panel panel--middle">
    <div class="frame motto serif-italic">Maintaining<br>driving independence<br>while leading<br>safe and<br>productive<br>lives!</div>
    <p class="contact contact__lead">For more information:</p>
    <p class="contact contact__phone">
      <svg width="17" height="17" viewBox="0 0 24 24" aria-hidden="true"><path fill="none" stroke="#fff" stroke-width="2" d="M6.5 3.5l3 3.5-2 2.2c1.2 2.6 3.2 4.6 5.8 5.8l2.2-2 3.5 3-1.6 3C11 19.5 4.5 13 3.5 5.1z"/><path fill="none" stroke="#fff" stroke-width="1.6" d="M14 3.5a6.5 6.5 0 0 1 6.5 6.5M14 7a3 3 0 0 1 3 3"/></svg>
      555-014-2290
    </p>
    <p class="contact contact__web">www.lanechangedriving.ca</p>
    <p class="contact contact__mail">mhale@lanechangedriving.ca</p>
  </div>

  <div class="panel panel--right">
    <div class="frame cover-title serif-italic">TURNING<br>POINT</div>
    <p class="cover-kicker">A 1-DAY EDUCATIONAL COURSE<br>FOR THOSE CHARGED WITH</p>
    <p class="cover-subject">DRIVING ON A<br>SUSPENDED LICENCE</p>
    <div class="frame brand">
      <span class="brand__mark"></span>
      <span class="brand__name">Lane Change<br>Driving School</span>
    </div>
    <svg class="cover-art" role="img" aria-label="Illustration of two hands gripping a steering wheel" viewBox="0 0 246 162" preserveAspectRatio="none">
      <defs><linearGradient id="wheelTone" x1="0" y1="0" x2="1" y2="1"><stop offset="0" stop-color="#2f6fb8"/><stop offset="1" stop-color="#1d4f95"/></linearGradient></defs>
      <path d="M0 162V60C60 20 190 10 246 50V162Z" fill="url(#wheelTone)" opacity=".55"/>
    </svg>
  </div>
</section>

<section class="sheet sheet--inside" aria-label="Brochure inside">
  <div class="panel panel--left">
    <div class="inside-text">
      <h2 class="inside-title serif-italic">SUSPENDED LICENCE-<br>TURNING POINT</h2>
      <p class="intro">During the course we will:</p>
      <h3>Defensive Driving module (The Big 4):</h3>
      <p>I. Lane position (better to drop 2 wheels on the shoulder than hit an oncoming vehicle)</p>
      <p>II. Following distance (varies depending on speed and conditions); space cushion driving (always have an out)</p>
      <p>III. Defensive stopping (what should we do every time we apply brakes?)</p>
      <p>IV. Strategic driving / what we do with our eyes:</p>
      <h3>Law:</h3>
      <p>I. Highway Traffic Act (privilege vs right); Federal &amp; Provincial; ways we can lose our license</p>
      <p>II. Implications of a criminal record (relationships, work, financial)</p>
      <h3>Road Rage:</h3>
      <p>I. Defining the continuum of road rage and escalation of anger</p>
      <p>II. Triggers</p>
      <p>III. Personality types (Type A); Holmes &amp; Rahe stress scale</p>
      <p>IV. Aggressive driving (overlap between aggressors and victims); reframing our views</p>
      <p>V. Psychiatric issues/PTSD: Not uncommon to have professional drivers come through the course due to over-exposure to stress from driving (both on the job and/or the commute to their driving job)</p>
    </div>
  </div>

  <div class="panel panel--middle">
    <div class="inside-text inside-text--middle">
      <h3 style="margin-top:0">Physiology of aggressive driving and how it affects the body:</h3>
      <p>I. Window of tolerance (hyper-arousal vs hypo-arousal)</p>
      <p>II. Fight or flight response: how it works</p>
      <p>III. Stress hormones (Adrenaline, Cortisol, Norepinephrine)</p>
      <p>IV. Chronic levels of exposure/Immune system suppression</p>
      <p>V. Hypertension</p>
      <p>VI. Sympathetic nervous system</p>
      <p>VII. Substances - will do an overview of alcohol/drinking and driving if relevant; individual and general factors that contribute to B.A.C</p>
      <h3>Personal context (risk vs protective factors); incumbent upon us to consider:</h3>
      <div class="tight">
        <p>I. Genetics (chemical predispositions)</p>
        <p>II. Socialization (role models)</p>
        <p>III. Environment</p>
      </div>
      <h3 style="margin-top:16px">Strategies to manage:</h3>
      <p>I. Stages of change theory; habit formation and how to reprogram (many of our decisions on any day are subconscious i.e., no decision-making process)</p>
      <p>II. Neuroplasticity and habit formation</p>
      <p>III. Supernormal stimuli: how our bodies have not kept up to the complexities of today’s society and its stresses</p>
      <p>IV. Ensure cerebral part of brain is making decisions and not “lizard” part of brain (amygdala vs cerebrum and their roles in the body); triggers &amp; stressors</p>
    </div>
  </div>

  <div class="panel panel--right">
    <div class="frame one-on-one serif-italic">COURSES ARE<br>ONE-ON-ONE</div>
    <svg class="remote-icon" role="img" aria-label="Icon of a person on a computer screen with a chat bubble" viewBox="0 0 74 74">
      <rect x="4" y="20" width="52" height="36" rx="3" fill="#10233f"/>
      <rect x="38" y="4" width="30" height="24" rx="6" fill="#ffffff"/>
    </svg>
    <p class="remote-label"><span class="dark">OFFERED</span><span>REMOTELY!</span></p>
    <div class="course-art" role="img" aria-label="Illustration of online learning with a presenter and a student at a laptop" style="background:linear-gradient(135deg,#e8f0f7 0%,#cfe0ee 100%);opacity:.9"></div>
    <div class="cost"><span class="cost__label">Course Cost:</span><span class="cost__value">$775.00 + HST</span></div>
  </div>
</section>

</body>
</html>
```